依頼概要
■ 依頼の目的/概要

ロゴが新しくなりましたので、そのロゴを使った新しい名刺をデザインしていただきたく、依頼させていただきました。たくさんのご提案よろしくお願い致します。

■ 名刺に記載する情報

会社名/役職/氏名/住所/電話/Fax/携帯/Mail/HP

■ 名刺デザインへの要望

ロゴの筆文字と調和した、スタイリッシュでインパクトのあるデザインを希望します。
色は色見本のような青系、もしくは暖色系の名刺にしたいと考えています。
ちなみにロゴの筆文字はベースと考えていただき、色の変更や立体化など自由に加工してかまいません。
またイカの絵はデザインの中に自由に組み込んでください。

■ 納品ファイルの希望

高解像度のjpg形式と、イラストレーター形式またはフォトショップ形式の2つ。
※実際に納品いただく際は印刷屋さんにそのまま入稿できる完全データでお願いします

■ 進め方

弊社の希望するイメージに近い提案を1つ(場合によって複数)選択させて頂きます。希望に近づけるために、修正要望を個別にさせて頂くこともあります。コンペ方式のため、修正後に当選されない場合も、どうかご了承ください。

■ その他/注意点

選択させて頂いた名刺デザインの著作権(財産権)等の扱いはBrivanz利用規約に従い、弊社に譲渡をお願いします。フォントや画像素材などを利用する場合は上記利用用途に使用できることを確認し、第三者の知的財産権等に注意して下さい。
依頼公開後の追記内容
ご説明が不十分で申し訳ございませんでした。本デザインではロゴの柳瀬水産という筆文字の下にある「yanasesuisan」というローマ字は抜いてください。(jpg画像のような形。aiやepsファイルには付いたままですので消してください)
また、デザイン的に英字が必要であれば、デザインに合った違う書体を使っていただくことは全然かまいませんのでご自由にご提案ください。それでは引き続きよろしくお願い致します。
説明不足で申し訳ございませんでしたが、aiやepsファイルにある四角い枠に囲まれたイカはロゴマークとは違いますので、あくまで「柳瀬水産」という筆文字だけをロゴ(タイプ)としてご使用ください。
イカの絵は自由な形でデザインに組み込めるように添付したものですので、必要であれば素材としてご活用していただきたいと思います。ちなみに当社はイカを使った商品が主ですので、今回イカの絵(オリジナル)を添付致しました。
■ 選んだ理由

シンプルにまとめたデザインで内容も見やすく整理されており、単色ながらベタ塗りのインパクトもありそうでしたのでこちらを選ばさせていただきました。素晴らしいご提案ありがとうございました。

■ 提案者全員へのお礼・コメント

この度はたくさんのご提案ありがとうございました。
どなたの作品もとてもきれいで、社内でもものすごく悩みましたが、当選者は1人に絞るということに決めていましたので、今回はお一人様のみに限定させていただきました。当選とならなかったブリヴァンザー様、当コンペに貴重なお時間をさいていただき本当にありがとうございました。近々、また別のデザインで依頼させていただく予定ですので、よろしければまたのご参加お待ちしております。ありがとうございました。

```html
<!DOCTYPE html>
<html lang="ja">
<head>
<meta charset="utf-8">
<title>柳瀬水産 名刺</title>
<link rel="stylesheet" href="https://fonts.googleapis.com/css2?family=Noto+Serif+JP:wght@500;900&family=Noto+Sans+JP:wght@400&display=swap">
<style>
  :root {
    --brand-red: #b5121b;
    --paper: #ececec;
    --ink: #1a1a1a;
    --white: #ffffff;
  }
  html, body {
    margin: 0;
    padding: 0;
    width: 719px;
    height: 1200px;
    overflow: hidden;
    background: var(--white);
  }
  .card {
    position: relative;
    width: 719px;
    height: 1200px;
    background: var(--paper);
    overflow: hidden;
  }
  .top-band {
    position: absolute;
    left: 0; top: 0;
    width: 100%; height: 53px;
    background: var(--brand-red);
  }
  .squid-art {
    position: absolute;
    left: 190px; top: 360px;
    width: 440px; height: 640px;
  }
  .company-name {
    position: absolute;
    left: 58px; top: 150px;
    margin: 0;
    font-family: "Noto Serif JP", serif;
    font-weight: 900;
    font-size: 132px;
    line-height: 1;
    letter-spacing: 2px;
    color: var(--brand-red);
  }
  .title {
    position: absolute;
    left: 400px; top: 380px;
    writing-mode: vertical-rl;
    font-family: "Noto Serif JP", serif;
    font-weight: 500;
    font-size: 36px;
    letter-spacing: 4px;
    color: var(--ink);
  }
  .person-name {
    position: absolute;
    left: 430px; top: 430px;
    margin: 0;
    writing-mode: vertical-rl;
    font-family: "Noto Serif JP", serif;
    font-weight: 500;
    font-size: 46px;
    letter-spacing: 62px;
    color: var(--ink);
  }
  .contact {
    position: absolute;
    left: 0; bottom: 0;
    width: 100%; height: 215px;
    background: var(--brand-red);
    box-sizing: border-box;
    padding: 20px 0 0 58px;
    font-family: "Noto Sans JP", sans-serif;
    font-size: 29px;
    line-height: 43px;
    color: var(--white);
  }
  .contact p { margin: 0; white-space: nowrap; }
  .contact .gap { margin-left: 32px; }
  .contact .web { margin-left: 78px; }
</style>
</head>
<body>
  <main class="card">
    <div class="top-band"></div>

    <svg class="squid-art" role="img" aria-label="イカのイラスト" viewBox="0 0 440 640">
      <defs>
        <radialGradient id="squidGlow" cx="50%" cy="45%" r="60%">
          <stop offset="0%" stop-color="#ffffff"/>
          <stop offset="100%" stop-color="#ececec"/>
        </radialGradient>
      </defs>
      <rect width="440" height="640" rx="40" fill="url(#squidGlow)"/>
    </svg>

    <h1 class="company-name">柳瀬水産</h1>

    <div class="title">代表取締役</div>
    <h2 class="person-name">柳瀬社長</h2>

    <footer class="contact">
      <p>□□県□□□□□□□□□□□□□□□□□</p>
      <p>電話 0000-00-0000<span class="gap">Fax0000-00-0000</span></p>
      <p>携帯 000-0000-0000</p>
      <p>Mail 00000000000<span class="web">HP 00000000000</span></p>
    </footer>
  </main>
</body>
</html>
```